Skincare,Bodycare and haircare brochure

Please design a A4 3 fold brochure for Vexmira Pty Ltd. You may go to our website www.vexmira.example to understand what we do - certified organic skincare.
Content:

About Us: Our Mission
Vexmira’s mission is to make premium skin care products using only certified organic ingredients for a safer, purer world.

How are we diferent?
Vexmira specialises in the research and development of certified organic skin, hair and personal care products for everyone. We hold Certified Organic Licenses with the Verdant Tally Board who accredits our system with the Federal Harvest Purity Code of Australia and other international organic certification standards. Vexmira’s passion is to produce and deliver premium, safe and effective certified organic products to all of our customers.

Other headings: Skincare, Body Care, Hair Care, Essential Oils (leave room for us to put product pictures and product info (you can copy 3 products from each category from our website for draft),

Please provide a heading about our memberships: Please also see our website for info.

Then have a contact us section (doesn't have to be a page) It can even be on the front page.

Please also use the Attached logos. Please use vexmira logo with underline (company logo) and dunbrook crafted and Certified Organic logos.

Many deaigns dont allow me to put alotnof product infronation on it. please allow me to donsoMan

```html
<!DOCTYPE html>
<html lang="en">
<head>
<meta charset="utf-8">
<title>Vexmira Pty Ltd – Tri-fold Brochure</title>
<link rel="stylesheet" href="https://fonts.googleapis.com/css2?family=Open+Sans:wght@400;600;700;800&display=swap">
<style>
  :root{
    --stage:#d8dbde;
    --charcoal:#3a3d40;
    --charcoal-dark:#2c2e30;
    --green:#8cc63f;
    --green-deep:#6ea62b;
    --paper:#ffffff;
    --paper-grey:#e8e9ea;
    --ink:#3a3d40;
    --ink-soft:#6b6e71;
    --price-dark:#5a2c2c;
    --bottle-amber:#6b3f22;
    --bottle-cap:#1f1f1f;
    --jar-body:#9aa0a3;
    --jar-lid:#3c3f41;
    --photo-skin:#d9b59a;
    --photo-warm:#b98a68;
  }
  *{box-sizing:border-box;margin:0;padding:0}
  html,body{width:1200px;height:800px;overflow:hidden}
  body{background:var(--stage);font-family:"Open Sans",Arial,sans-serif;color:var(--ink)}

  .brochure{position:absolute;left:45px;top:30px;width:1110px;height:740px;display:flex;box-shadow:0 10px 30px rgba(0,0,0,.18)}
  .panel{position:relative;width:370px;height:740px;overflow:hidden;background:var(--paper)}

  /* ---------- About panel ---------- */
  .panel--about{background:var(--charcoal);padding:26px 26px 20px;color:#e9eaeb}
  .about-heading{color:var(--green);font-size:13px;font-weight:800;text-transform:uppercase;letter-spacing:.3px;margin:10px 0 4px}
  .about-heading:first-child{margin-top:0}
  .about-heading span{text-transform:none}
  .about-text{font-size:10.3px;line-height:1.5;color:#e4e5e6}

  /* ---------- Shared product styles ---------- */
  .product{display:flex;flex-direction:column;align-items:center;text-align:center;width:74px}
  .pack{border-radius:4px}
  .pack--bottle{width:26px;height:72px;border-radius:4px 4px 5px 5px;background:linear-gradient(180deg,var(--bottle-cap) 0 26%,var(--bottle-amber) 26% 100%)}
  .pack--tall{width:30px;height:92px;border-radius:4px;background:linear-gradient(180deg,var(--bottle-cap) 0 18%,var(--bottle-amber) 18% 100%)}
  .pack--tube{width:26px;height:80px;border-radius:3px 3px 8px 8px;background:linear-gradient(180deg,#f2efe8 0 82%,#c9c3b6 82% 100%)}
  .pack--jar{width:52px;height:52px;border-radius:6px;background:linear-gradient(180deg,var(--jar-lid) 0 30%,var(--jar-body) 30% 100%)}
  .product-name{font-size:8.5px;font-weight:700;text-transform:uppercase;line-height:1.2;margin-top:6px;color:var(--ink)}
  .price{display:flex;align-items:center;justify-content:center;width:22px;height:22px;border-radius:50%;background:var(--green);color:#fff;font-size:8.5px;font-weight:700;margin-top:5px}
  .price--dark{background:var(--price-dark)}

  .section-title{font-weight:800;text-transform:uppercase;letter-spacing:.2px;line-height:1.05}

  /* ---------- Middle panel ---------- */
  .panel--essentials{background:var(--paper)}
  .oils-area{position:absolute;left:0;top:0;width:370px;height:228px;background:linear-gradient(180deg,#d9dadb,var(--paper-grey))}
  .oils-area .section-title{position:absolute;left:26px;top:24px;font-size:20px;color:var(--ink)}
  .oils-row{position:absolute;left:14px;right:14px;top:64px;display:flex;justify-content:space-around}

  .spa-photo{position:absolute;left:0;top:228px;width:370px;height:178px;background:linear-gradient(120deg,#efe6dd,var(--photo-skin) 55%,var(--photo-warm))}
  .body-care-label{position:absolute;right:0;top:255px;width:140px;height:96px;background:var(--green);display:flex;align-items:center;padding-left:18px}
  .body-care-label .section-title{color:#fff;font-size:16px}

  .facial-photo{position:absolute;left:0;top:406px;width:210px;height:200px;background:linear-gradient(135deg,#f4ece4,var(--photo-skin) 60%,#c9a487)}
  .skin-care-heading{position:absolute;left:150px;top:440px;font-size:19px;color:var(--ink-soft)}
  .skin-feature{position:absolute;left:250px;top:500px}
  .skin-row{position:absolute;left:30px;right:40px;top:620px;display:flex;justify-content:space-between}

  /* ---------- Right panel ---------- */
  .panel--catalogue{background:var(--paper)}
  .hair-band{position:absolute;left:0;top:0;width:370px;height:50px;background:var(--charcoal)}
  .hair-band .section-title{position:absolute;left:26px;top:16px;font-size:17px;color:#fff}
  .massage-photo{position:absolute;right:-20px;top:-30px;width:140px;height:110px;border-radius:50%;border:5px solid var(--charcoal);background:linear-gradient(140deg,#e4c7ab,var(--photo-warm))}
  .hair-row{position:absolute;left:40px;top:62px;display:flex;gap:14px}

  .body-band{position:absolute;left:0;top:210px;width:370px;height:138px;background:var(--green)}
  .body-row{position:absolute;left:8px;right:8px;top:222px;display:flex;justify-content:space-between}
  .body-row .product{width:68px}
  .body-row .product-name{color:#fff}

  .skin-grid{position:absolute;left:24px;right:24px;top:380px;display:grid;grid-template-columns:repeat(3,1fr);row-gap:34px;justify-items:center}
  .skin-grid .product{width:96px}
</style>
</head>
<body>
<main class="brochure">

  <!-- About panel -->
  <section class="panel panel--about">
    <h2 class="about-heading">About Us: <span>Our Mission</span></h2>
    <p class="about-text">Vexmira’s mission is to make premium skin care products using only certified organic ingredients for a safer, purer world.</p>

    <h2 class="about-heading">How are we different?</h2>
    <p class="about-text">Vexmira specialises in the research and development of certified organic skin, hair and personal care products for everyone. We hold Certified Organic Licenses with the Verdant Tally Board who accredits our system with the Federal Harvest Purity Code of Australia and other international organic certification standards. Vexmira’s passion is to produce and deliver premium, safe and effective certified organic products to all of our customers.</p>

    <h2 class="about-heading">Why certified organic?</h2>
    <p class="about-text">Many companies label their products with words such as natural, yet these claims are rarely checked. Certified organic products are audited from soil to shelf, so every ingredient is grown, processed and packed without synthetic chemicals, giving you a product you can truly trust.</p>

    <h2 class="about-heading">Soil</h2>
    <p class="about-text">The soil of certified organic farms is managed through crop rotation, compost and green manure to keep it rich and alive. Healthy soil grows stronger plants, locks in carbon and protects local waterways from harmful runoff, supporting a cleaner environment for generations to come.</p>

    <h2 class="about-heading">Pest control</h2>
    <p class="about-text">Certified organic growers manage pests with natural predators, companion planting and careful timing rather than synthetic sprays. This protects bees, birds and beneficial insects, keeps residues out of our ingredients and helps farms remain balanced, productive and resilient season after season.</p>

    <h2 class="about-heading">Production</h2>
    <p class="about-text">Genetically modified organisms are strictly excluded at every stage of production. Vexmira sources its certified ingredients from trusted growers who share our values.</p>
  </section>

  <!-- Essential oils / body / skin panel -->
  <section class="panel panel--essentials">
    <div class="oils-area">
      <h2 class="section-title">Essential Oils</h2>
      <div class="oils-row">
        <div class="product"><div class="pack pack--bottle" role="img" aria-label="Clementine essential oil bottle"></div><p class="product-name">Clementine</p><span class="price">$18</span></div>
        <div class="product"><div class="pack pack--bottle" role="img" aria-label="Lemon grass essential oil bottle"></div><p class="product-name">Lemon Grass</p><span class="price">$16</span></div>
        <div class="product"><div class="pack pack--bottle" role="img" aria-label="Lemon myrtle essential oil bottle"></div><p class="product-name">Lemon Myrtle</p><span class="price">$18</span></div>
        <div class="product"><div class="pack pack--bottle" role="img" aria-label="Ylang ylang essential oil bottle"></div><p class="product-name">Ylang Ylang</p><span class="price">$22</span></div>
      </div>
    </div>

    <div class="spa-photo" role="img" aria-label="Photo of a woman relaxing at a spa"></div>
    <div class="body-care-label"><h2 class="section-title">Body Care<br>Products</h2></div>

    <div class="facial-photo" role="img" aria-label="Photo of a woman receiving a facial treatment"></div>
    <h2 class="section-title skin-care-heading">Skin Care<br>Products</h2>
    <div class="product skin-feature"><div class="pack pack--jar" role="img" aria-label="Moisturising cream jar"></div><p class="product-name">Moisturising Cream</p><span class="price">$45</span></div>

    <div class="skin-row">
      <div class="product"><div class="pack pack--jar" role="img" aria-label="Skin brightening serum jar"></div><p class="product-name">Skin Brightening Serum</p><span class="price">$52</span></div>
      <div class="product"><div class="pack pack--jar" role="img" aria-label="Antioxidant primer jar"></div><p class="product-name">Australian Antioxidant Primer</p><span class="price">$48</span></div>
    </div>
  </section>

  <!-- Hair / body / skin catalogue panel -->
  <section class="panel panel--catalogue">
    <div class="hair-band"><h2 class="section-title">Hair Care Products</h2></div>
    <div class="massage-photo" role="img" aria-label="Photo of a relaxing back massage"></div>
    <div class="hair-row">
      <div class="product"><div class="pack pack--tall" role="img" aria-label="Shampoo bottle"></div><p class="product-name">Shampoo</p><span class="price">$28</span></div>
      <div class="product"><div class="pack pack--tall" role="img" aria-label="Conditioner bottle"></div><p class="product-name">Conditioner</p><span class="price">$28</span></div>
    </div>

    <div class="body-band"></div>
    <div class="body-row">
      <div class="product"><div class="pack pack--tall" role="img" aria-label="Shower gel bottle"></div><p class="product-name">Shower Gel</p><span class="price price--dark">$24</span></div>
      <div class="product"><div class="pack pack--jar" role="img" aria-label="Certified organic body lotion jar"></div><p class="product-name">Certified Organic Body Lotion</p><span class="price price--dark">$35</span></div>
      <div class="product"><div class="pack pack--jar" role="img" aria-label="Body custard jar"></div><p class="product-name">Body Custard</p><span class="price price--dark">$38</span></div>
      <div class="product"><div class="pack pack--tube" role="img" aria-label="Hand cream tube"></div><p class="product-name">Hand Cream</p><span class="price price--dark">$22</span></div>
      <div class="product"><div class="pack pack--jar" role="img" aria-label="Body scrub jar"></div><p class="product-name">Body Scrub</p><span class="price price--dark">$32</span></div>
    </div>

    <div class="skin-grid">
      <div class="product"><div class="pack pack--jar" role="img" aria-label="Organic eye cream jar"></div><p class="product-name">Organic Eye Cream</p><span class="price">$46</span></div>
      <div class="product"><div class="pack pack--jar" role="img" aria-label="Organic lip balm jar"></div><p class="product-name">Organic Lip Balm</p><span class="price">$12</span></div>
      <div class="product"><div class="pack pack--jar" role="img" aria-label="Organic aloe vera gel jar"></div><p class="product-name">Organic Aloe Vera Gel</p><span class="price">$26</span></div>
      <div class="product"><div class="pack pack--jar" role="img" aria-label="Makeup remover jar"></div><p class="product-name">Makeup Remover Wildflower Extract</p><span class="price">$30</span></div>
      <div class="product"><div class="pack pack--jar" role="img" aria-label="Rose face exfoliant jar"></div><p class="product-name">Rose Canola Face Exfoliant</p><span class="price">$34</span></div>
      <div class="product"><div class="pack pack--jar" role="img" aria-label="Antioxidant facial mask jar"></div><p class="product-name">Antioxidant Boost Facial</p><span class="price">$42</span></div>
    </div>
  </section>

</main>
</body>
</html>
```